Corporate Profile
Advisory Services Firm
The main purpose of this marketing collateral is to provide a document that sales staff can leave with customers after an appointment.
Corporate Services
Senior executives. A typical reader of this material will be in a decision making role within a large organisation (more than 500 employees).
Maximum eight pages (including front and rear cover.
Consistent in theme and style with the Amber Fern website
Sections to include:
Front cover (quirky and interesting, perhaps also using the ‘tree and grass’ image from the website
Company profile (who we are and what we do, using the values from the website- single page
Advisory services (six key areas, from the website) – double page
Making a difference (selected success stories and customer quotes) – double page spread
Tallyforge Suite (product overview and list of frameworks) – double page spread
Amber Fern in the community (using information from the website) – single page
Back page (contact details, website details, what else?)
FORMAT
Finished product to be provided in Adobe InDesign CS5 file format, although proofs can be delivered as PDF files.
Primary colour palette is
TS Green
C 50
M 0
Y 85
B 0
TS Grey
M 40
Y 40
B 20
TS Blue (complementary, not main)
C 73.79
M 55.26
Y 16.58
B 1.22
SUPPORTING INFORMATION PROVIDED
Amber Fern website address: www.amberfern-studio.com.au
Tallyforge Suite website mockups: please request from morwenk@amberfern-studio.com.au
Sample page showing required information on the Tallyforge Suite spread. Taken from various pages on www.tallyforgesuite.com.au:8081/

```html
<!DOCTYPE html>
<html lang="en">
<head>
<meta charset="utf-8">
<title>Amber Fern – Advisory Services</title>
<link rel="stylesheet" href="https://fonts.googleapis.com/css2?family=Jost:ital,wght@0,400;0,500;0,600;1,600&display=swap">
<style>
  :root{
    --ts-green:#8cc63f;
    --ts-blue:#1f7bbf;
    --ink:#2f2f2f;
    --text-grey:#6b6b6b;
    --shade:#f1f1f1;
    --bar-light:#c4c4c4;
    --bar-dark:#4d4d4d;
    --canvas:#e9e9e9;
  }
  *{box-sizing:border-box;margin:0;padding:0}
  html,body{width:1200px;height:780px;overflow:hidden;background:var(--canvas)}
  body{font-family:"Jost",sans-serif;color:var(--text-grey);display:flex;gap:8px;padding:5px 6px}
  .page{position:relative;width:590px;height:770px;background:#fff;overflow:hidden}
  .masthead{position:relative;height:140px;display:flex}
  .masthead-block{width:226px;background:var(--ts-blue)}
  .masthead-band{flex:1;background:var(--ts-green);position:relative}
  .masthead-title{position:absolute;left:22px;top:52px;font-weight:500;font-size:22px;letter-spacing:.3px;color:var(--ink)}
  .masthead-photo{position:absolute;right:10px;top:12px;width:112px;height:116px;background:linear-gradient(160deg,#d9e3ea,#8aa5b8 60%,#5d7585)}
  .brand{position:absolute;left:18px;top:150px;display:flex;align-items:center;gap:7px;font-weight:500;font-size:19px;letter-spacing:1.5px;color:var(--ts-blue)}
  .brand-mark{width:10px;height:10px;background:var(--ts-blue)}
  .columns{position:absolute;left:0;right:0;top:140px;bottom:30px;display:flex}
  .column{flex:1;padding:58px 12px 0 14px}
  .column--shaded{background:var(--shade)}
  .column-icon{display:block;width:64px;height:64px;margin:0 auto 8px;border:1px solid #ddd}
  .caption{text-align:center;margin-bottom:22px;line-height:1.15}
  .caption-key{display:block;font-style:italic;font-weight:600;font-size:13px;color:var(--ts-blue)}
  .caption-sub{font-size:11px;color:var(--text-grey)}
  .service{margin-bottom:18px}
  .service-title{font-weight:600;font-size:12.5px;color:var(--ts-green);margin-bottom:2px}
  .service-list{list-style:none;font-size:10.5px;line-height:13px}
  .footer-bar{position:absolute;left:0;right:0;bottom:12px;height:12px;display:flex}
  .footer-bar-light{width:34%;background:var(--bar-light)}
  .footer-bar-dark{flex:1;background:var(--bar-dark)}
</style>
</head>
<body>

<section class="page">
  <header class="masthead">
    <div class="masthead-block"></div>
    <div class="masthead-band">
      <h1 class="masthead-title">ADVISORY SERVICES</h1>
      <div class="masthead-photo" role="img" aria-label="Photo of a handshake emerging from a laptop screen"></div>
    </div>
  </header>
  <div class="columns">
    <div class="column">
      <div class="column-icon" role="img" aria-label="Photo of yellow rubber ducks in a row" style="background:linear-gradient(#fff3b0,#f2c230)"></div>
      <p class="caption"><span class="caption-key">understand how</span><span class="caption-sub">governance</span></p>
      <div class="service"><h2 class="service-title">corporate governance</h2>
        <ul class="service-list"><li>corporate governance</li><li>public sector governance</li><li>policy and standards</li><li>project governance</li><li>benchmarking</li><li>information management</li><li>value management</li></ul></div>
      <div class="service"><h2 class="service-title">conduct governance</h2>
        <ul class="service-list"><li>corporate conduct</li><li>employee relations</li><li>board/committee guidance</li><li>whistle blower programs</li><li>employer industrial advocacy</li></ul></div>
      <div class="service"><h2 class="service-title">technology governance</h2>
        <ul class="service-list"><li>ICT governance</li><li>ICT policy and standards</li><li>ICT benchmarking</li><li>information security management</li><li>transition planning</li></ul></div>
    </div>
    <div class="column column--shaded">
      <div class="column-icon" role="img" aria-label="Photo of a warning sign" style="background:linear-gradient(#f4f4f4,#cfcfcf)"></div>
      <p class="caption"><span class="caption-key">manage risk</span><span class="caption-sub">risk</span></p>
      <div class="service"><h2 class="service-title">corporate risk</h2>
        <ul class="service-list"><li>risk management</li><li>risk/threat assessment</li><li>compliance frameworks</li><li>regulatory compliance</li><li>standards compliance</li><li>project assurance</li><li>audit/investigation services</li></ul></div>
      <div class="service"><h2 class="service-title">conduct risk</h2>
        <ul class="service-list"><li>fraud risk management</li><li>standards monitoring</li><li>contract investigations</li><li>industrial relations</li><li>forensic investigations</li></ul></div>
      <div class="service"><h2 class="service-title">technology risk</h2>
        <ul class="service-list"><li>ICT risk management</li><li>ICT security assessments</li><li>ICT project/standards assurance</li><li>ICT standards compliance</li><li>ICT audit services</li></ul></div>
    </div>
    <div class="column">
      <div class="column-icon" role="img" aria-label="Illustration of a standout figure among a group" style="background:linear-gradient(#c8e59a,#7fb241)"></div>
      <p class="caption"><span class="caption-key">be different</span><span class="caption-sub">strategy</span></p>
      <div class="service"><h2 class="service-title">corporate strategy</h2>
        <ul class="service-list"><li>strategic planning</li><li>balanced scorecard</li><li>business continuity</li><li>research services</li><li>business architecture</li><li>portfolio management</li></ul></div>
      <div class="service"><h2 class="service-title">conduct strategy</h2>
        <ul class="service-list"><li>misconduct resistance</li><li>complaints management</li><li>workplace grievances</li><li>staff training/development</li><li>mediation services</li></ul></div>
      <div class="service"><h2 class="service-title">technology strategy</h2>
        <ul class="service-list"><li>ICT strategic planning</li><li>CIO services</li><li>information architecture</li><li>ICT sustainability</li><li>disaster recovery</li></ul></div>
    </div>
  </div>
  <div class="brand"><span class="brand-mark"></span>AMBER FERN</div>
  <div class="footer-bar"><div class="footer-bar-light"></div><div class="footer-bar-dark"></div></div>
</section>

<section class="page">
  <header class="masthead">
    <div class="masthead-block"></div>
    <div class="masthead-band">
      <h1 class="masthead-title">ADVISORY SERVICES</h1>
      <div class="masthead-photo" role="img" aria-label="Photo of a handshake emerging from a laptop screen"></div>
    </div>
  </header>
  <div class="columns">
    <div class="column">
      <div class="column-icon" role="img" aria-label="Illustration of blue figures forming a strong group" style="background:linear-gradient(#cfe2f3,#3f86c6)"></div>
      <p class="caption"><span class="caption-key">stronger</span><span class="caption-sub">corporate advisory</span></p>
      <div class="service"><h2 class="service-title">corporate governance</h2>
        <ul class="service-list"><li>corporate governance</li><li>public sector governance</li><li>policy and standards</li><li>project governance</li><li>benchmarking</li><li>information management</li><li>value management</li></ul></div>
      <div class="service"><h2 class="service-title">corporate strategy</h2>
        <ul class="service-list"><li>strategic planning</li><li>balanced scorecard</li><li>business continuity</li><li>research services</li><li>business architecture</li><li>portfolio management</li><li>business process modelling</li></ul></div>
      <div class="service"><h2 class="service-title">corporate risk</h2>
        <ul class="service-list"><li>risk management</li><li>risk/threat assessments</li><li>compliance frameworks</li><li>regulatory compliance</li><li>standards compliance</li><li>project assurance</li><li>audit/investigation services</li></ul></div>
    </div>
    <div class="column column--shaded">
      <div class="column-icon" role="img" aria-label="Illustration of a figure stepping ahead" style="background:linear-gradient(#e4e4e4,#9a9a9a)"></div>
      <p class="caption"><span class="caption-key">better</span><span class="caption-sub">professional conduct</span></p>
      <div class="service"><h2 class="service-title">conduct governance</h2>
        <ul class="service-list"><li>corporate conduct</li><li>employee relations</li><li>board/committee guidance</li><li>whistle blower programs</li><li>employer industrial advocacy</li></ul></div>
      <div class="service"><h2 class="service-title">conduct strategy</h2>
        <ul class="service-list"><li>misconduct resistance</li><li>complaints management</li><li>workplace grievances</li><li>staff training/development</li><li>mediation services</li></ul></div>
      <div class="service"><h2 class="service-title">conduct risk</h2>
        <ul class="service-list"><li>fraud risk management</li><li>standards monitoring</li><li>contract investigations</li><li>industrial relations</li><li>forensic investigations</li></ul></div>
    </div>
    <div class="column">
      <div class="column-icon" role="img" aria-label="Illustration of a figure running forward" style="background:linear-gradient(#dce9f5,#6f9ccc)"></div>
      <p class="caption"><span class="caption-key">faster</span><span class="caption-sub">technology advisory</span></p>
      <div class="service"><h2 class="service-title">technology governance</h2>
        <ul class="service-list"><li>ICT governance</li><li>ICT policy and standards</li><li>ICT benchmarking</li><li>information security management</li><li>transition planning</li></ul></div>
      <div class="service"><h2 class="service-title">technology strategy</h2>
        <ul class="service-list"><li>ICT strategic planning</li><li>CIO services</li><li>information architecture</li><li>ICT sustainability</li><li>disaster recovery</li></ul></div>
      <div class="service"><h2 class="service-title">technology risk</h2>
        <ul class="service-list"><li>ICT risk management</li><li>ICT security assessments</li><li>ICT project/standards assurance</li><li>ICT standards compliance</li><li>ICT audit services</li></ul></div>
    </div>
  </div>
  <div class="brand"><span class="brand-mark"></span>AMBER FERN</div>
  <div class="footer-bar"><div class="footer-bar-light"></div><div class="footer-bar-dark"></div></div>
</section>

</body>
</html>
```